Fruit Juice packaging for Canada Market

We need label designs for our Fruit juice in PET form and we have 6 flavours ( tamarind, Blueberry, Passion Fruit+ Mango, Cucumis Melo+green tea, Mulberry, and Mango.
We need designs for packaging for all 6 listed fruits

1) Blueberry Juice labeling.
2) Tamarind Juice labeling.
3) Mulberry Juice labeling.
4) Passion fruit + Mango Juice labeling.
5) Cucumis Melo+green tea Juice labeling.
6) Mango Juice labeling.

A: PET bottle shape and dimensions:
- Dimensions: please refer to attachment name: VERUMO Bottle shape
- Bottle shape: Please refer to attachment name: BOTTLE SHAPE for the actual look of the bottle design.

B: Design Ideal: we want to have a look of fresh and juicy of real fruits since we are producing RAW juices. You can chose any taken photo of fruits on Pixelharbor. (http://www.pixelharbor-example.com/photos/blueberry?phrase=Blueberry&excludenudity=true&sort=best)

C: Fonts will be up to the designer choose, easy to read, neat and easy recognize

D: Label content needs to have followings: please refer to attachment VERUMO SAMPLE DESIGN for all needed information.
Main licence Company: HARLOWE Trading Inc.
Product Name: VERUMO
Product Name1 : Verumo Blueberry Juice (attached)
Flavor Name 1 : Blueberry
and
Product Name 2 : Verumo Tamarind Juice (attached)
Flavor Name 2: Tamarind
...and so on for the rest of juices

I want the design in English with editable Ai or PTS so that I can add shortly Vietnamese translation text as mandatory law in our current market-Vietnam. We will take care the translation for you.

Old labels are attached to give you an idea. Contents in the old will be pasted in your labels (nutrition facts, net weight, ingredient, direction of use... etc). you re-design to make it fresher and healthier.

On the label for 330ml PET bottle, (please see picture of sample bottle), decal dimension of L:17.5cm x H:12cm following phrase must be included:

- Made of Real Fruit Juice

- Direction of use: will be provided in Ai.
- Ingredients: will be provided in Ai.

- Production and Packaging under licence of
DORVEN INC., CANADA
452 Rue Fenwick Ouest, Quebec, CANADA.

- Importing, Producing and Distributing by PRELOM Ltd.,
- Km7, Lac Son town, Ho Chi Minh, Viet Nam.
- Made in Vietnam

- Nutrition Fact ( Canada label requirements)
- HALAL logo ( will be provided, show at front and on the back)
- ISO 22000:2005 logo (will be provided )
-Manufacturing date/Used by date: on the cap.
-Keep refrigerated for an even better taste.

(Somewhere in Front)

0% Cholesterol
Blueberry imports from CANADA. (for Blueberry Juice)
Delicious Tamarind from VIETNAM. ( for Tamarind juice)
Has HALAL logo at front ( see provided picture for reference)
picture of juice, fresh, wet fruits around the bottom bottle.
running juice from the juice at the bottom to the cap.

(P/S: the label packaging must meet the standard requirement for Canada)
Please request me for more info if needed.

VIETNAM and NORTH AMERICA

Pet

Serif
Sans Serif
Decorative
Script
Other font styles liked:
• Prefer to designers to chose on their design to make it looks match

Designer to choose colors to be used in the design.

• meet Canada Labeling requirement for imported products.
• Ai editable version is a must to allow us to add Vietnamese translation and movable objects on the packaging design after we add Vietnamese text.
• have done any packaging with Canadian customers with Nutrition Facts on.

```html
<!DOCTYPE html>
<html lang="en">
<head>
<meta charset="utf-8">
<title>Verumo Fresh Juice – 330mL Label Range</title>
<link href="https://fonts.googleapis.com/css2?family=Questrial&display=swap" rel="stylesheet">
<style>
  :root{
    --stage:#eef1f4;
    --cap:#5de85f;
    --label-light:#ffffff;
    --label-edge:#e4e4e6;
    --fresh-grey:#5b5b60;
    --brand-ink:#3a3a3e;
    --halal-green:#1f6a3a;
    --volume-red:#c8453a;
  }
  *{margin:0;padding:0;box-sizing:border-box}
  html,body{width:1200px;height:682px;overflow:hidden}
  body{background:var(--stage);font-family:"Questrial",sans-serif;position:relative}

  .bottle{position:absolute;top:84px;width:160px;height:550px}
  .bottle-shape{position:absolute;inset:0;width:160px;height:550px}
  .bottle-shape .body{fill:var(--body)}
  .bottle-shape .cap{fill:var(--cap)}

  .label{position:absolute;left:0;top:132px;width:160px;height:376px;
    background:linear-gradient(90deg,var(--label-edge) 0%,var(--label-light) 45%,var(--label-light) 60%,var(--label-edge) 100%);
    text-align:center;color:var(--fresh-grey)}

  .splash{position:absolute;left:22px;top:30px;width:118px;height:112px;border-radius:50%;
    background:radial-gradient(ellipse at center,var(--splash) 0%,rgba(255,255,255,0) 70%);opacity:.55}
  .brand{position:absolute;left:0;right:0;top:72px;font-size:26px;letter-spacing:.5px;color:var(--brand-ink)}

  .fresh{position:absolute;left:0;right:0;top:166px;font-size:32px;letter-spacing:1px;line-height:1}
  .flavour{position:absolute;left:0;right:0;top:202px;font-size:16px;line-height:1.15;color:var(--flavour)}
  .flavour .spaced{letter-spacing:9px;padding-left:9px}
  .flavour .small{font-size:14px}

  .fruit-photo{position:absolute;left:12px;top:262px;width:138px;height:62px;border-radius:30px;
    background:radial-gradient(ellipse at center,var(--fruit) 0%,var(--fruit) 45%,rgba(255,255,255,0) 75%)}
  .halal-badge{position:absolute;left:6px;top:326px;width:38px;height:38px;border-radius:50%;
    background:var(--halal-green);border:3px solid #fff;box-shadow:0 0 0 1px var(--halal-green)}
  .volume{position:absolute;left:0;right:0;top:330px;font-size:8px;color:var(--volume-red);padding-left:8px}
  .juice-flow{position:absolute;left:0;right:0;bottom:0;height:44px;
    background:linear-gradient(180deg,rgba(255,255,255,0) 0%,var(--splash) 100%);opacity:.45}

  .melo{left:60px;--body:#fbd384;--flavour:#ef8d3a;--splash:#e8c43a;--fruit:#f2a066}
  .tamarind{left:240px;--body:#e7b352;--flavour:#8b4a2a;--splash:#e0b83a;--fruit:#9a6a3c}
  .mulberry{left:420px;--body:#8f3a9f;--flavour:#3d4aa0;--splash:#5a78c8;--fruit:#2e2a34}
  .blueberry{left:600px;--body:#a24ab8;--flavour:#3d4aa0;--splash:#5a78c8;--fruit:#4a5f98}
  .mango{left:782px;--body:#f6b634;--flavour:#f08a3c;--splash:#e8c43a;--fruit:#f2a63a}
  .passion{left:960px;--body:#f6cf7c;--flavour:#5a2a45;--splash:#e8c43a;--fruit:#7a4a5a}
</style>
</head>
<body>

<svg width="0" height="0" style="position:absolute">
  <defs>
    <symbol id="bottle-outline" viewBox="0 0 160 550">
      <path class="body" d="M44 40 H116 V54 C116 82 160 92 160 132 V530 Q160 550 140 550 H20 Q0 550 0 530 V132 C0 92 44 82 44 54 Z"/>
      <rect class="cap" x="36" y="0" width="88" height="42" rx="6"/>
      <rect class="cap" x="32" y="34" width="96" height="10" rx="4"/>
    </symbol>
  </defs>
</svg>

<div class="bottle melo">
  <svg class="bottle-shape" viewBox="0 0 160 550"><use href="#bottle-outline"/></svg>
  <div class="label">
    <div class="splash" role="img" aria-label="Golden juice splash around the brand name"></div>
    <div class="brand">VERUMO</div>
    <div class="fresh">FRESH</div>
    <div class="flavour"><span class="small">CUCUMISMELO</span><br><span class="small">GREEN TEA</span><br><span class="spaced">JUICE</span></div>
    <div class="fruit-photo" role="img" aria-label="Sliced cantaloupe melon, cucumber and tea leaves"></div>
    <div class="halal-badge"></div>
    <div class="volume">330mL</div>
    <div class="juice-flow" role="img" aria-label="Flowing golden juice along the label base"></div>
  </div>
</div>

<div class="bottle tamarind">
  <svg class="bottle-shape" viewBox="0 0 160 550"><use href="#bottle-outline"/></svg>
  <div class="label">
    <div class="splash" role="img" aria-label="Golden juice splash around the brand name"></div>
    <div class="brand">VERUMO</div>
    <div class="fresh">FRESH</div>
    <div class="flavour"><span class="spaced" style="letter-spacing:2px;padding-left:2px">TAMARIND</span><br><span class="spaced">JUICE</span></div>
    <div class="fruit-photo" role="img" aria-label="Open tamarind pods with leaves"></div>
    <div class="halal-badge"></div>
    <div class="volume">330mL</div>
    <div class="juice-flow" role="img" aria-label="Flowing tamarind juice along the label base"></div>
  </div>
</div>

<div class="bottle mulberry">
  <svg class="bottle-shape" viewBox="0 0 160 550"><use href="#bottle-outline"/></svg>
  <div class="label">
    <div class="splash" role="img" aria-label="Blue water splash around the brand name"></div>
    <div class="brand">VERUMO</div>
    <div class="fresh">FRESH</div>
    <div class="flavour"><span class="spaced" style="letter-spacing:2px;padding-left:2px">MULBERRY</span><br><span class="spaced">JUICE</span></div>
    <div class="fruit-photo" role="img" aria-label="Ripe dark mulberries with a leaf"></div>
    <div class="halal-badge"></div>
    <div class="volume">330ML</div>
    <div class="juice-flow" role="img" aria-label="Flowing blue water along the label base"></div>
  </div>
</div>

<div class="bottle blueberry">
  <svg class="bottle-shape" viewBox="0 0 160 550"><use href="#bottle-outline"/></svg>
  <div class="label">
    <div class="splash" role="img" aria-label="Blue water splash around the brand name"></div>
    <div class="brand">VERUMO</div>
    <div class="fresh">FRESH</div>
    <div class="flavour"><span class="spaced" style="letter-spacing:1px;padding-left:1px">BLUEBERRY</span><br><span class="spaced">JUICE</span></div>
    <div class="fruit-photo" role="img" aria-label="Fresh blueberries with leaves"></div>
    <div class="halal-badge"></div>
    <div class="volume">330mL</div>
    <div class="juice-flow" role="img" aria-label="Flowing blue water along the label base"></div>
  </div>
</div>

<div class="bottle mango">
  <svg class="bottle-shape" viewBox="0 0 160 550"><use href="#bottle-outline"/></svg>
  <div class="label">
    <div class="splash" role="img" aria-label="Golden juice splash around the brand name"></div>
    <div class="brand">VERUMO</div>
    <div class="fresh">FRESH</div>
    <div class="flavour"><span class="spaced">MANGO</span><br><span class="spaced">JUICE</span></div>
    <div class="fruit-photo" role="img" aria-label="Whole and halved ripe mangoes"></div>
    <div class="halal-badge"></div>
    <div class="volume">330mL</div>
    <div class="juice-flow" role="img" aria-label="Flowing golden juice along the label base"></div>
  </div>
</div>

<div class="bottle passion">
  <svg class="bottle-shape" viewBox="0 0 160 550"><use href="#bottle-outline"/></svg>
  <div class="label">
    <div class="splash" role="img" aria-label="Golden juice splash around the brand name"></div>
    <div class="brand">VERUMO</div>
    <div class="fresh">FRESH</div>
    <div class="flavour"><span class="small">PASSION FRUIT</span><br><span style="letter-spacing:2px">&amp; MANGO</span><br><span class="spaced">JUICE</span></div>
    <div class="fruit-photo" role="img" aria-label="Halved passion fruit and a ripe mango"></div>
    <div class="halal-badge"></div>
    <div class="volume">330ML</div>
    <div class="juice-flow" role="img" aria-label="Flowing golden juice along the label base"></div>
  </div>
</div>

</body>
</html>
```